GlowMoths Windows App design

We will need a designer to redesign our entire app for Windows Phone use.

Currently, we have apps available for Android and iOS, they can be downloaded here: http://www.talvorin.net/downloads/

Other than just following the same concept, we want this app to be based on the Metro design, with an about page to tell user more about this app and our services, also to design the live tile.

Included are some designs done previously by other designers.
Updates

Dear Designers,

We would be making our decision based on the main screen, where device list is loaded. 

The main direction would be the metro style design.

Best Regards,
Merrow

Reason: We have pretty good designs in, just a few more days to see if there are any new entrants.

Industry/Entity Type

Android

```html
<!DOCTYPE html>
<html lang="en">
<head>
<meta charset="utf-8">
<title>GlowMoths – Devices</title>
<link href="https://fonts.googleapis.com/css2?family=Open+Sans:wght@300;400&display=swap" rel="stylesheet">
<style>
  :root {
    --canvas: #dfdfdf;
    --surface: #ffffff;
    --ink: #3a3a3a;
    --ink-soft: #555555;
    --muted: #bdbdbd;
    --accent: #5ad6d2;
    --focus: #e8141e;
    --status-warn: #e8a030;
    --status-alert: #c8252d;
    --status-ok: #4fa83a;
  }
  * { box-sizing: border-box; margin: 0; padding: 0; }
  html, body { width: 1200px; height: 960px; overflow: hidden; }
  body {
    background: var(--canvas);
    font-family: "Open Sans", sans-serif;
    font-weight: 300;
    color: var(--ink);
    position: relative;
  }
  .app-frame {
    position: absolute;
    left: 148px; top: 286px;
    width: 902px; height: 451px;
    background: var(--surface);
    box-shadow: 0 1px 2px rgba(0,0,0,.15);
  }
  .brand {
    position: absolute; left: 12px; top: 20px;
    font-size: 23px; font-weight: 400;
    letter-spacing: 34px; color: var(--accent);
    line-height: 1; white-space: nowrap;
  }
  .section-title {
    font-size: 28px; font-weight: 300; line-height: 1;
    margin-bottom: 12px;
  }
  .devices-pane {
    position: absolute; left: -1px; top: -1px;
    width: 303px; height: 453px;
    border: 2px solid var(--focus);
    box-shadow: 0 10px 24px rgba(0,0,0,.12);
    padding: 62px 0 0 11px;
  }
  .welcome { font-size: 19px; line-height: 1; margin-bottom: 15px; }
  .welcome .user { color: var(--accent); }
  .device-list { list-style: none; }
  .device {
    position: relative;
    height: 37px; margin-bottom: 10px;
    padding-left: 15px;
    border-left: 4px solid var(--status-ok);
  }
  .device.warn { border-color: var(--status-warn); }
  .device.alert { border-color: var(--status-alert); }
  .device-name { font-size: 18.5px; line-height: 20px; color: var(--ink); font-weight: 400; }
  .device-address {
    font-size: 11px; line-height: 14px; color: var(--ink-soft);
    white-space: nowrap; width: 190px; overflow: hidden; text-overflow: ellipsis;
  }
  .device-open { position: absolute; left: 220px; top: 4px; width: 30px; height: 30px; }
  .device-total { font-size: 18.5px; color: var(--accent); margin-top: -4px; }
  .info-pane { position: absolute; top: 62px; color: var(--muted); z-index: 1; }
  .info-pane .section-title { color: var(--muted); }
  .about-pane { left: 286px; width: 272px; }
  .logout-pane { left: 586px; width: 250px; }
  .info-text { font-size: 14px; line-height: 18px; }
</style>
</head>
<body>
  <main class="app-frame">
    <div class="brand">GlowMoths</div>

    <section class="devices-pane">
      <h1 class="section-title">devices</h1>
      <p class="welcome">Welcome, <span class="user">user876</span></p>
      <ul class="device-list">
        <li class="device warn"><div class="device-name">Device name</div><div class="device-address">14 Harlow Quay Road 9, Vantria</div><svg class="device-open" viewBox="0 0 30 30"><circle cx="15" cy="15" r="13" fill="none" stroke="#444" stroke-width="2.4"/><path d="M8 15h13M16 10l5 5-5 5" fill="none" stroke="#444" stroke-width="2.4"/></svg></li>
        <li class="device warn"><div class="device-name">Device name</div><div class="device-address">14 Harlow Quay Road 9, Vantria</div><svg class="device-open" viewBox="0 0 30 30"><circle cx="15" cy="15" r="13" fill="none" stroke="#444" stroke-width="2.4"/><path d="M8 15h13M16 10l5 5-5 5" fill="none" stroke="#444" stroke-width="2.4"/></svg></li>
        <li class="device alert"><div class="device-name">Device name</div><div class="device-address">14 Harlow Quay Road 9, Vantria</div><svg class="device-open" viewBox="0 0 30 30"><circle cx="15" cy="15" r="13" fill="none" stroke="#444" stroke-width="2.4"/><path d="M8 15h13M16 10l5 5-5 5" fill="none" stroke="#444" stroke-width="2.4"/></svg></li>
        <li class="device alert"><div class="device-name">Device name</div><div class="device-address">14 Harlow Quay Road 9, Vantria</div><svg class="device-open" viewBox="0 0 30 30"><circle cx="15" cy="15" r="13" fill="none" stroke="#444" stroke-width="2.4"/><path d="M8 15h13M16 10l5 5-5 5" fill="none" stroke="#444" stroke-width="2.4"/></svg></li>
        <li class="device"><div class="device-name">Device name</div><div class="device-address">14 Harlow Quay Road 9, Vantria</div><svg class="device-open" viewBox="0 0 30 30"><circle cx="15" cy="15" r="13" fill="none" stroke="#444" stroke-width="2.4"/><path d="M8 15h13M16 10l5 5-5 5" fill="none" stroke="#444" stroke-width="2.4"/></svg></li>
        <li class="device"><div class="device-name">Device name</div><div class="device-address">14 Harlow Quay Road 9, Vantria</div><svg class="device-open" viewBox="0 0 30 30"><circle cx="15" cy="15" r="13" fill="none" stroke="#444" stroke-width="2.4"/><path d="M8 15h13M16 10l5 5-5 5" fill="none" stroke="#444" stroke-width="2.4"/></svg></li>
      </ul>
      <p class="device-total">Total Device : 6 Devices</p>
    </section>

    <section class="info-pane about-pane">
      <h2 class="section-title">about</h2>
      <p class="info-text">This is Draftwell's version of Lorem Ipsum. Proin gravida nibh vel velit auctor aliquet. Aenean sollicitudin, lorem quis bibendum auctor, nisi elit consequat ipsum, nec sagittis sem nibh id elit. Duis sed odio sit amet nibh vulputate cursus a sit amet mauris. Morbi accumsan ipsum velit. Nam nec tellus a odio tincidunt auctor a ornare odio. Sed non mauris vitae erat consequat auctor eu in elit. Class aptent taciti sociosqu ad litora torquent per conubia nostra, per inceptos himenaeos. Mauris in erat justo. Nullam ac urna eu felis dapibus condimentum sit amet a augue. Sed non neque elit. Sed ut imperdiet nisi. Proin condimentum fermentum nunc. Etiam pharetra, erat sed fermentum feugiat,</p>
    </section>

    <section class="info-pane logout-pane">
      <h2 class="section-title">logout</h2>
      <p class="info-text">Take care &amp; goodbye.</p>
    </section>
  </main>
</body>
</html>
```